Startup company business card (Media & Advertising)

we need a business card design for a company that is a startup in the media and aggregation industry. Card needs to look funky and of a new breed/modern and upmarket.

Target Market(s)

advertisers/ brand agencies & media publishers

Industry/Entity Type

Advertising

Contact Information for Business Card

Please ensure the front face signifies our brand (plumvexo.com) and back has details for the contact. Standard contact such as phone , address, email , website etc.

Font styles to use
Other font styles liked:
• use styleguide and logo font and color

Colors

Designer to choose colors to be used in the design.

Requirements
Must have
• We are disrupting the media and agency industry so subtlety would be good to use imagery to signify this
Nice to have
• Please use logo colors for branding
Should not have
• be as creative and provide few options. Pick a brand color from logo and styleguide

```html
<!DOCTYPE html>
<html lang="en">
<head>
<meta charset="utf-8">
<title>plumvexo business card</title>
<link rel="stylesheet" href="https://fonts.googleapis.com/css2?family=Lato:wght@400;700;900&display=swap">
<style>
  :root {
    --bg: #3a3a3c;
    --card-dark: #070709;
    --card-light: #ffffff;
    --brand-red: #e8243c;
    --ink: #111111;
    --muted: #4a4a4a;
    --on-dark: #f2f2f2;
  }
  * { box-sizing: border-box; margin: 0; padding: 0; }
  html, body {
    width: 1200px; height: 900px; overflow: hidden;
    background: var(--bg);
    font-family: "Lato", sans-serif;
  }
  .stage {
    position: relative; width: 1200px; height: 900px;
    display: flex; flex-direction: column; align-items: center; justify-content: center; gap: 40px;
  }
  .card {
    width: 620px; height: 354px; border-radius: 18px;
    position: relative; overflow: hidden;
    box-shadow: 0 10px 28px rgba(0,0,0,0.45);
  }

  /* Brand side */
  .card--brand {
    background: var(--card-dark); color: var(--on-dark);
    display: flex; flex-direction: column; align-items: center; justify-content: center; gap: 42px;
  }
  .wordmark {
    display: flex; align-items: center; gap: 16px;
    font-family: "Lato", sans-serif; font-weight: 900; letter-spacing: 0.5px;
  }
  .wordmark__dot {
    width: 52px; height: 52px; border-radius: 50%; background: var(--brand-red); flex: none;
  }
  .card--brand .wordmark { font-size: 54px; color: var(--on-dark); }
  .tagline {
    text-align: center; font-size: 13.5px; line-height: 1.45; color: var(--on-dark);
  }

  /* Contact side */
  .card--contact {
    background: var(--card-light); color: var(--ink);
    display: flex; align-items: center;
  }
  .card--contact .wordmark {
    font-size: 40px; color: var(--ink);
    width: 305px; justify-content: center; margin-top: 48px;
  }
  .card--contact .wordmark__dot { width: 40px; height: 40px; }
  .divider {
    width: 2px; height: 200px; background: var(--brand-red); flex: none;
  }
  .details { padding-left: 34px; padding-bottom: 30px; }
  .details__name {
    font-weight: 900; font-size: 29px; color: var(--brand-red); letter-spacing: 0.3px; line-height: 1.05;
  }
  .details__role { font-size: 15px; color: var(--muted); margin-top: 2px; }
  .details__address { font-size: 15px; color: var(--muted); line-height: 1.25; margin-top: 14px; }
  .contact-list { list-style: none; margin-top: 10px; }
  .contact-list li {
    display: flex; align-items: center; gap: 12px;
    font-size: 15px; color: var(--muted); line-height: 1.45;
  }
  .contact-list svg { width: 15px; height: 15px; flex: none; }
  .accent { color: var(--brand-red); }
</style>
</head>
<body>
<main class="stage">

  <section class="card card--brand" aria-label="Brand side">
    <div class="wordmark"><span class="wordmark__dot"></span><span>plumvexo</span></div>
    <p class="tagline">
      Find, compare and select your media, and plan your campaign<br>
      View their rates, and then provide/create your advertisements using our simple editor<br>
      Make your payment, go live, and measure your success.
    </p>
  </section>

  <section class="card card--contact" aria-label="Contact side">
    <div class="wordmark"><span class="wordmark__dot"></span><span>plumvexo</span></div>
    <div class="divider"></div>
    <div class="details">
      <h1 class="details__name">ELIAS MARLOW</h1>
      <p class="details__role">Founder &amp; CEO</p>
      <p class="details__address">1234 First Line Address<br>5678 Second Line Address</p>
      <ul class="contact-list">
        <li>
          <svg viewBox="0 0 24 24" aria-hidden="true"><path fill="#e8243c" d="M6.6 10.8a15.1 15.1 0 0 0 6.6 6.6l2.2-2.2a1 1 0 0 1 1-.25 11.4 11.4 0 0 0 3.6.57 1 1 0 0 1 1 1V20a1 1 0 0 1-1 1A17 17 0 0 1 3 4a1 1 0 0 1 1-1h3.5a1 1 0 0 1 1 1c0 1.25.2 2.45.57 3.57a1 1 0 0 1-.25 1z"/></svg>
          1234567890
        </li>
        <li>
          <svg viewBox="0 0 24 24" aria-hidden="true"><rect x="2" y="5" width="20" height="14" rx="1.5" fill="#e8243c"/><path d="M3 6.5l9 6.5 9-6.5" fill="none" stroke="#fff" stroke-width="1.6"/></svg>
          info@plumvexo.com
        </li>
        <li>
          <svg viewBox="0 0 24 24" aria-hidden="true"><g fill="none" stroke="#e8243c" stroke-width="1.8"><circle cx="12" cy="12" r="9.5"/><ellipse cx="12" cy="12" rx="4" ry="9.5"/><path d="M2.5 12h19M4 7h16M4 17h16"/></g></svg>
          <span>www.<span class="accent">plumvexo</span>.com</span>
        </li>
      </ul>
    </div>
  </section>

</main>
</body>
</html>
```